Business Card Design Project

I have had my current business card for 6years and it is time to upgrade my business card. I have uploaded my old card
I am a retail specialty shop designer and want something designer looking but professional.
Target Market(s)
30-60 year old people in retail businesses
Industry/Entity Type
Retail
Requirements
Must have
- The Vela Fitouts logo (but colour can and style can be altered)
My name, position and contact details as per my existing card attached .
Rupert Calloway Director
m: 0418536771
rupert@velafitouts.com.au
www.velafitouts.com.au
t:02 94417268 f: 02 94417293
po box 817 harlowe vale nsw 1490
Nice to have
- Use both sides of the card

```html
<!DOCTYPE html>
<html lang="en">
<head>
<meta charset="utf-8">
<title>Vela Fitouts – Business Card</title>
<link href="https://fonts.googleapis.com/css2?family=Inter:wght@300;400&display=swap" rel="stylesheet">
<style>
  :root {
    --stage: #3a3a3a;
    --card-deep: #0a3f9e;
    --card-mid: #1f6fd6;
    --card-light: #4d9bf0;
    --mark: #161616;
    --text: #ffffff;
    --text-soft: #cfe2ff;
  }
  * { margin: 0; padding: 0; box-sizing: border-box; }
  html, body {
    width: 1200px;
    height: 456px;
    overflow: hidden;
    background: var(--stage);
    font-family: "Inter", Helvetica, Arial, sans-serif;
    font-weight: 300;
  }
  .stage {
    position: relative;
    width: 1200px;
    height: 456px;
  }
  .card {
    position: absolute;
    top: 73px;
    width: 506px;
    height: 308px;
    border-radius: 20px;
    overflow: hidden;
    color: var(--text);
    background:
      radial-gradient(circle at 18% 78%, rgba(160, 205, 255, 0.45) 0, rgba(160, 205, 255, 0) 38%),
      radial-gradient(circle at 80% 22%, rgba(120, 185, 255, 0.35) 0, rgba(120, 185, 255, 0) 42%),
      radial-gradient(ellipse at 55% 55%, var(--card-light) 0, var(--card-mid) 45%, var(--card-deep) 100%);
  }
  .card--front { left: 80px; }
  .card--back  { left: 616px; }

  .brand {
    position: absolute;
    display: flex;
    align-items: center;
    gap: 12px;
    transform: translate(-50%, -50%);
  }
  .brand__square {
    width: 26px;
    height: 26px;
    background: var(--mark);
    flex: none;
  }
  .brand__name {
    font-size: 30px;
    font-weight: 300;
    letter-spacing: 1px;
    color: var(--text);
    white-space: nowrap;
  }
  .card--front .brand {
    left: 50%;
    top: 50%;
  }
  .card--back .brand {
    left: 110px;
    top: 157px;
    gap: 10px;
  }
  .card--back .brand__name { font-size: 21px; }
  .card--back .brand__square { width: 19px; height: 19px; }

  .contact {
    position: absolute;
    left: 237px;
    top: 60px;
  }
  .contact__name {
    font-size: 23px;
    font-weight: 300;
    line-height: 1.1;
  }
  .contact__role {
    font-size: 16px;
    color: var(--text-soft);
    margin-top: 2px;
  }
  .contact__details {
    list-style: none;
    margin-top: 36px;
    font-size: 14.5px;
    line-height: 18px;
    color: var(--text-soft);
    white-space: nowrap;
  }
</style>
</head>
<body>
  <main class="stage">
    <section class="card card--front" aria-label="Card front">
      <div class="brand">
        <span class="brand__square"></span>
        <span class="brand__name">Vela Fitouts</span>
      </div>
    </section>

    <section class="card card--back" aria-label="Card back">
      <div class="brand">
        <span class="brand__square"></span>
        <span class="brand__name">Vela Fitouts</span>
      </div>
      <div class="contact">
        <p class="contact__name">Rupert Calloway</p>
        <p class="contact__role">Director</p>
        <ul class="contact__details">
          <li>PO box 817 harlowe vale nsw 1490</li>
          <li>M: 0418 536 771</li>
          <li>T: (02) 9441 7268</li>
          <li>F: (02) 9441 7293</li>
          <li>rupert@velafitouts.com.au</li>
          <li>www.velafitouts.com.au</li>
        </ul>
      </div>
    </section>
  </main>
</body>
</html>
```